Brinwood Roofing & Exteriors

Need a nice clean/creative/ classy truck wrap to stand out. I like how in the photos of my logo (black) the logo is also incorporated into background almost like a shadow. I drive a 2018 white crew cab Corvane talwick 2400
Target Market(s)
Anyone looking to have home improvents done
Industry/Entity Type
Construction
Colors
Designer to choose colors to be used in the design.
Requirements
Must have
- Phone # 620-555-0193 maybe a QR code to www.brinwoodexteriorsllc.com
Nice to have
- Advertising for roofing,siding,windows,concrete,painting
Should not have
- I don't want a wrap to make me seem like a low end /cheap contractor. I want a high end contractor look.

```html
<!DOCTYPE html>
<html lang="en">
<head>
<meta charset="utf-8">
<title>Brinwood Roofing &amp; Exteriors – Truck Wrap Layout</title>
<link rel="stylesheet" href="https://fonts.googleapis.com/css2?family=Montserrat:wght@500;600&display=swap">
<style>
  :root {
    --page-bg: #e6e6e6;
    --wrap-black: #050608;
    --stripe-grey: #5c5c5c;
    --type-white: #ffffff;
  }
  html, body {
    margin: 0;
    padding: 0;
    width: 1200px;
    height: 1000px;
    overflow: hidden;
    background: var(--page-bg);
  }
  .canvas {
    position: relative;
    width: 1200px;
    height: 1000px;
    display: flex;
    align-items: center;
  }
  .wrap-panel {
    display: block;
    width: 1200px;
    height: 386px;
    font-family: "Montserrat", Arial, sans-serif;
  }
  .wrap-panel__base { fill: var(--wrap-black); }
  .stripe { fill: var(--stripe-grey); }
  .brand-name,
  .brand-line {
    fill: var(--type-white);
    font-weight: 600;
  }
  .brand-name { font-size: 84px; }
  .brand-line { font-size: 30px; letter-spacing: 4px; }
  .phone {
    fill: var(--type-white);
    font-weight: 500;
    font-size: 56px;
    letter-spacing: 6px;
  }
  .services text {
    fill: var(--type-white);
    font-weight: 500;
    font-size: 27px;
    letter-spacing: 3px;
  }
</style>
</head>
<body>
<main class="canvas">
  <svg class="wrap-panel" viewBox="0 0 2100 675" xmlns="http://www.w3.org/2000/svg" aria-labelledby="wrap-title">
    <title id="wrap-title">Brinwood Roofing &amp; Exteriors flat truck wrap layout</title>
    <rect class="wrap-panel__base" x="0" y="0" width="2100" height="675"/>

    <g class="stripes">
      <polygon class="stripe" points="958,0 1012,0 938,82 884,82"/>
      <polygon class="stripe" points="1110,0 1165,0 1090,82 1035,82"/>
      <polygon class="stripe" points="556,187 572,187 400,390 384,390"/>
      <polygon class="stripe" points="638,190 653,190 484,390 468,390"/>
      <polygon class="stripe" points="1822,305 1822,385 1745,482 1668,482"/>
      <polygon class="stripe" points="1700,262 1760,262 1585,482 1520,482"/>
    </g>

    <g class="brand">
      <text class="brand-name" x="772" y="407" textLength="450" lengthAdjust="spacingAndGlyphs">BRINWOOD</text>
      <text class="brand-line" x="775" y="446" textLength="444" lengthAdjust="spacingAndGlyphs">ROOFING &amp; EXTERIORS</text>
    </g>

    <text class="phone" x="775" y="540" textLength="442" lengthAdjust="spacingAndGlyphs">620-555-0193</text>

    <g class="services" transform="translate(1405,355) rotate(-47)">
      <text x="0" y="0">ROOFING</text>
      <text x="40" y="34">SIDING</text>
      <text x="20" y="68">WINDOWS</text>
      <text x="30" y="102">CONCRETE</text>
      <text x="60" y="136">PAINTING</text>
    </g>
  </svg>
</main>
</body>
</html>
```